Sleep Consulting Business

Hello I need a business card design with similar colors to my logo that was created. I help mom/parents whose little ones are having sleep issues. Are you able to recreate the picture with the girl sleeping onto a business card using a picture that I provide. That would be one side with my logo on top and on the other side would the following:
My name (in bigger letters than the rest. maybe written in script
title
email
website
phone
instagram
I have included color Inspo
Contact Information for Business Card
Full Name, number, email, website, ig page
Look and feel
Each slider illustrates characteristics of the customer's brand and the style your logo design should communicate.

```html
<!DOCTYPE html>
<html lang="en">
<head>
<meta charset="utf-8">
<title>Quiet Dawn – Business Card Colourways</title>
<link rel="stylesheet" href="https://fonts.googleapis.com/css2?family=Lato:wght@400;700&family=Kaushan+Script&display=swap">
<style>
  :root {
    --board: #6d6d6d;
    --white: #ffffff;
    --rust: #a3532f;
    --umber: #a18663;
    --mist: #c4b7ae;
    --clay: #d38b6b;
    --sand: #cfb7a0;
    --apricot: #d8976d;
    --taupe: #9e918a;
    --latte: #c2a78a;
    --blush: #d1927f;
    --linen: #d5c8bf;
  }
  * { box-sizing: border-box; margin: 0; padding: 0; }
  html, body { width: 766px; height: 1200px; overflow: hidden; background: var(--board); }
  .board { position: relative; width: 766px; height: 1200px; font-family: "Lato", sans-serif; }

  .card {
    position: absolute; width: 258px; height: 148px; border-radius: 8px;
    overflow: hidden;
  }
  .card--front { left: 89px; background: var(--card-bg); color: var(--white); }
  .card--back { left: 401px; background: var(--white); }

  .label {
    position: absolute; width: 258px; text-align: center;
    color: var(--white); font-size: 15px; letter-spacing: 0.3px;
  }
  .label--front { left: 89px; }
  .label--back { left: 401px; }

  /* front */
  .front-mark {
    position: absolute; left: 0; right: 0; top: 32px; text-align: center;
    font-size: 20px; font-weight: 700; letter-spacing: 1px; color: var(--white);
  }
  .front-mark .dot {
    display: inline-block; width: 14px; height: 14px; border-radius: 50%;
    background: var(--white); margin-right: 6px; vertical-align: -1px;
  }
  .holder { position: absolute; right: 142px; top: 96px; text-align: right; }
  .holder-name { font-family: "Kaushan Script", cursive; font-size: 13px; line-height: 1.1; }
  .holder-title { font-size: 6px; letter-spacing: 0.3px; }
  .divider { position: absolute; left: 128px; top: 92px; width: 0.6px; height: 32px; background: var(--white); }
  .contacts { position: absolute; left: 140px; top: 93px; list-style: none; font-size: 5.4px; line-height: 8.3px; }
  .contacts li { display: flex; align-items: center; gap: 3px; }
  .contacts svg { width: 5px; height: 5px; flex: none; }

  /* back */
  .back-mark {
    position: absolute; left: 0; right: 0; top: 50px; text-align: center;
    font-size: 30px; font-weight: 700; letter-spacing: 1px; color: var(--mark);
  }
  .back-mark .dot {
    display: inline-block; width: 18px; height: 18px; border-radius: 50%;
    background: var(--accent); margin-right: 8px; vertical-align: -1px;
  }

  .row-1 { top: 67px; }  .row-1l { top: 220px; }
  .row-2 { top: 247px; } .row-2l { top: 400px; }
  .row-3 { top: 427px; } .row-3l { top: 581px; }
  .row-4 { top: 607px; } .row-4l { top: 759px; }
  .row-5 { top: 787px; } .row-5l { top: 939px; }
  .row-6 { top: 967px; } .row-6l { top: 1122px; }
</style>
</head>
<body>
<main class="board">

  <!-- colourway template repeated six times -->
  <section class="card card--front row-1" style="--card-bg: var(--rust)">
    <div class="front-mark"><span class="dot"></span>Quiet Dawn</div>
    <div class="holder"><p class="holder-name">Daniel Reyes</p><p class="holder-title">Founder &amp; CEO</p></div>
    <div class="divider"></div>
    <ul class="contacts">
      <li><svg viewBox="0 0 10 10"><path d="M2 1 L4 1 L5 3.5 L3.8 4.5 Q5 6.5 6 6.5 L7 5.2 L9 6.5 L9 8.5 Q4 9.5 1 2 Z" fill="#fff"/></svg>(555) 014-2290</li>
      <li><svg viewBox="0 0 10 10"><rect x="1" y="2.5" width="8" height="5.5" fill="#fff"/></svg>hello@quietdawnsleep.com</li>
      <li><svg viewBox="0 0 10 10"><circle cx="5" cy="5" r="4" fill="#fff"/></svg>quietdawnsleep.com</li>
      <li><svg viewBox="0 0 10 10"><circle cx="5" cy="5" r="3.3" fill="none" stroke="#fff" stroke-width="1.2"/></svg>@quietdawnsleep</li>
    </ul>
  </section>
  <section class="card card--back row-1" style="--mark: var(--rust); --accent: var(--latte)">
    <div class="back-mark"><span class="dot"></span>Quiet Dawn</div>
  </section>
  <p class="label label--front row-1l">FRONT 01</p>
  <p class="label label--back row-1l">BACK 01</p>

  <section class="card card--front row-2" style="--card-bg: var(--umber)">
    <div class="front-mark"><span class="dot"></span>Quiet Dawn</div>
    <div class="holder"><p class="holder-name">Daniel Reyes</p><p class="holder-title">Founder &amp; CEO</p></div>
    <div class="divider"></div>
    <ul class="contacts">
      <li><svg viewBox="0 0 10 10"><path d="M2 1 L4 1 L5 3.5 L3.8 4.5 Q5 6.5 6 6.5 L7 5.2 L9 6.5 L9 8.5 Q4 9.5 1 2 Z" fill="#fff"/></svg>(555) 014-2290</li>
      <li><svg viewBox="0 0 10 10"><rect x="1" y="2.5" width="8" height="5.5" fill="#fff"/></svg>hello@quietdawnsleep.com</li>
      <li><svg viewBox="0 0 10 10"><circle cx="5" cy="5" r="4" fill="#fff"/></svg>quietdawnsleep.com</li>
      <li><svg viewBox="0 0 10 10"><circle cx="5" cy="5" r="3.3" fill="none" stroke="#fff" stroke-width="1.2"/></svg>@quietdawnsleep</li>
    </ul>
  </section>
  <section class="card card--back row-2" style="--mark: var(--taupe); --accent: var(--blush)">
    <div class="back-mark"><span class="dot"></span>Quiet Dawn</div>
  </section>
  <p class="label label--front row-2l">FRONT 02</p>
  <p class="label label--back row-2l">BACK 02</p>

  <section class="card card--front row-3" style="--card-bg: var(--mist)">
    <div class="front-mark"><span class="dot"></span>Quiet Dawn</div>
    <div class="holder"><p class="holder-name">Daniel Reyes</p><p class="holder-title">Founder &amp; CEO</p></div>
    <div class="divider"></div>
    <ul class="contacts">
      <li><svg viewBox="0 0 10 10"><path d="M2 1 L4 1 L5 3.5 L3.8 4.5 Q5 6.5 6 6.5 L7 5.2 L9 6.5 L9 8.5 Q4 9.5 1 2 Z" fill="#fff"/></svg>(555) 014-2290</li>
      <li><svg viewBox="0 0 10 10"><rect x="1" y="2.5" width="8" height="5.5" fill="#fff"/></svg>hello@quietdawnsleep.com</li>
      <li><svg viewBox="0 0 10 10"><circle cx="5" cy="5" r="4" fill="#fff"/></svg>quietdawnsleep.com</li>
      <li><svg viewBox="0 0 10 10"><circle cx="5" cy="5" r="3.3" fill="none" stroke="#fff" stroke-width="1.2"/></svg>@quietdawnsleep</li>
    </ul>
  </section>
  <section class="card card--back row-3" style="--mark: var(--taupe); --accent: var(--linen)">
    <div class="back-mark"><span class="dot"></span>Quiet Dawn</div>
  </section>
  <p class="label label--front row-3l">FRONT 03</p>
  <p class="label label--back row-3l">BACK 03</p>

  <section class="card card--front row-4" style="--card-bg: var(--clay)">
    <div class="front-mark"><span class="dot"></span>Quiet Dawn</div>
    <div class="holder"><p class="holder-name">Daniel Reyes</p><p class="holder-title">Founder &amp; CEO</p></div>
    <div class="divider"></div>
    <ul class="contacts">
      <li><svg viewBox="0 0 10 10"><path d="M2 1 L4 1 L5 3.5 L3.8 4.5 Q5 6.5 6 6.5 L7 5.2 L9 6.5 L9 8.5 Q4 9.5 1 2 Z" fill="#fff"/></svg>(555) 014-2290</li>
      <li><svg viewBox="0 0 10 10"><rect x="1" y="2.5" width="8" height="5.5" fill="#fff"/></svg>hello@quietdawnsleep.com</li>
      <li><svg viewBox="0 0 10 10"><circle cx="5" cy="5" r="4" fill="#fff"/></svg>quietdawnsleep.com</li>
      <li><svg viewBox="0 0 10 10"><circle cx="5" cy="5" r="3.3" fill="none" stroke="#fff" stroke-width="1.2"/></svg>@quietdawnsleep</li>
    </ul>
  </section>
  <section class="card card--back row-4" style="--mark: var(--taupe); --accent: var(--clay)">
    <div class="back-mark"><span class="dot"></span>Quiet Dawn</div>
  </section>
  <p class="label label--front row-4l">FRONT 04</p>
  <p class="label label--back row-4l">BACK 04</p>

  <section class="card card--front row-5" style="--card-bg: var(--sand)">
    <div class="front-mark"><span class="dot"></span>Quiet Dawn</div>
    <div class="holder"><p class="holder-name">Daniel Reyes</p><p class="holder-title">Founder &amp; CEO</p></div>
    <div class="divider"></div>
    <ul class="contacts">
      <li><svg viewBox="0 0 10 10"><path d="M2 1 L4 1 L5 3.5 L3.8 4.5 Q5 6.5 6 6.5 L7 5.2 L9 6.5 L9 8.5 Q4 9.5 1 2 Z" fill="#fff"/></svg>(555) 014-2290</li>
      <li><svg viewBox="0 0 10 10"><rect x="1" y="2.5" width="8" height="5.5" fill="#fff"/></svg>hello@quietdawnsleep.com</li>
      <li><svg viewBox="0 0 10 10"><circle cx="5" cy="5" r="4" fill="#fff"/></svg>quietdawnsleep.com</li>
      <li><svg viewBox="0 0 10 10"><circle cx="5" cy="5" r="3.3" fill="none" stroke="#fff" stroke-width="1.2"/></svg>@quietdawnsleep</li>
    </ul>
  </section>
  <section class="card card--back row-5" style="--mark: var(--sand); --accent: var(--apricot)">
    <div class="back-mark"><span class="dot"></span>Quiet Dawn</div>
  </section>
  <p class="label label--front row-5l">FRONT 05</p>
  <p class="label label--back row-5l">BACK 05</p>

  <section class="card card--front row-6" style="--card-bg: var(--apricot)">
    <div class="front-mark"><span class="dot"></span>Quiet Dawn</div>
    <div class="holder"><p class="holder-name">Daniel Reyes</p><p class="holder-title">Founder &amp; CEO</p></div>
    <div class="divider"></div>
    <ul class="contacts">
      <li><svg viewBox="0 0 10 10"><path d="M2 1 L4 1 L5 3.5 L3.8 4.5 Q5 6.5 6 6.5 L7 5.2 L9 6.5 L9 8.5 Q4 9.5 1 2 Z" fill="#fff"/></svg>(555) 014-2290</li>
      <li><svg viewBox="0 0 10 10"><rect x="1" y="2.5" width="8" height="5.5" fill="#fff"/></svg>hello@quietdawnsleep.com</li>
      <li><svg viewBox="0 0 10 10"><circle cx="5" cy="5" r="4" fill="#fff"/></svg>quietdawnsleep.com</li>
      <li><svg viewBox="0 0 10 10"><circle cx="5" cy="5" r="3.3" fill="none" stroke="#fff" stroke-width="1.2"/></svg>@quietdawnsleep</li>
    </ul>
  </section>
  <section class="card card--back row-6" style="--mark: var(--rust); --accent: var(--apricot)">
    <div class="back-mark"><span class="dot"></span>Quiet Dawn</div>
  </section>
  <p class="label label--front row-6l">FRONT 06</p>
  <p class="label label--back row-6l">BACK 05</p>

</main>
</body>
</html>
```